Vellora - Quality health delivered at your door

Vellora offers home and Community Based Services for adults who wish to continue live independently in their communities. We increase accessibility to health care, reduce health care delivery gap, reduce mortality and morbidity, reduce health while promoting healthy living in the comfort of our patients communities or homes.

We provide on site services and deliver high quality healthcare at your door. Our experienced physicians coordinate care with our certified nurse practitioners and provide chronic care management, physical therapy, rehabilitation and medications management.

Target Market(s)

Older population living in independent living facilities

Industry/Entity Type

Health Care

Contact Information for Business Card

Vellora

Number of Pages Required

4 page

Font styles to use
Sans Serif

Colors

Designer to choose colors to be used in the design.

```html
<!DOCTYPE html>
<html lang="en">
<head>
<meta charset="utf-8">
<title>Vellora - Quality health delivered at your door</title>
<link href="https://fonts.googleapis.com/css2?family=Open+Sans:wght@400;600;700;800&display=swap" rel="stylesheet">
<style>
:root{
  --orange:#f39200;
  --orange-dark:#d97d00;
  --green:#8cc63f;
  --green-deep:#5a8a1f;
  --forest:#1f2a14;
  --forest-2:#2a3820;
  --ink:#2b2b2b;
  --muted:#666;
  --line:#e2e2e2;
  --white:#fff;
}
*{box-sizing:border-box;margin:0;padding:0}
html,body{width:870px;height:1200px;overflow:hidden}
body{font-family:"Open Sans",Arial,sans-serif;color:var(--ink);background:var(--white)}
.page{width:870px;height:1200px;position:relative}

.header{height:88px;display:flex;align-items:center;justify-content:space-between;padding:0 40px}
.brand{display:flex;align-items:center;gap:10px}
.brand-dot{width:30px;height:30px;border-radius:50%;background:var(--green)}
.brand-name{font-weight:700;font-size:20px;color:var(--green-deep);letter-spacing:1px}
.header-right{display:flex;align-items:center;gap:26px}
.follow{display:flex;align-items:center;gap:8px;font-size:10px;color:var(--muted);font-weight:600}
.social{width:24px;height:24px;border-radius:50%;background:#9aa0a6}
.call{display:flex;align-items:center;gap:8px}
.call-label{font-size:10px;color:var(--muted);line-height:1.2}
.call-number{font-size:16px;font-weight:700;color:var(--orange-dark);display:block}

.nav{height:36px;background:var(--orange);display:flex;align-items:center;justify-content:center;gap:0}
.nav a{color:var(--white);text-decoration:none;font-size:11px;font-weight:600;padding:0 13px;border-right:1px solid rgba(255,255,255,.4);line-height:36px}
.nav a:first-child{background:var(--orange-dark)}
.nav a:last-child{border-right:0}

.hero{height:360px;position:relative;background:linear-gradient(100deg,#e9b53a 0%,#b9a43c 35%,#6f8a3a 65%,#c9c8b0 100%)}
.hero-copy{position:absolute;left:45px;top:50px;width:430px}
.hero-title{font-size:42px;line-height:1.1;font-weight:700;color:#a4d65e;text-shadow:0 1px 2px rgba(0,0,0,.25)}
.hero-sub{margin-top:14px;font-size:14px;color:var(--white);line-height:1.5;font-weight:600}
.hero-actions{margin-top:30px;display:flex;gap:12px}
.btn{display:inline-block;font-size:12px;font-weight:700;color:var(--white);padding:11px 22px;border-radius:3px;text-transform:uppercase}
.btn-dark{background:var(--forest)}
.btn-orange{background:var(--orange)}

.services{padding-top:40px;text-align:center}
.section-title{font-size:32px;font-weight:400;letter-spacing:1px;color:var(--ink)}
.section-text{width:720px;margin:14px auto 0;font-size:11px;color:var(--muted);line-height:1.6}
.cards{position:relative;margin:26px auto 0;width:790px;display:flex;justify-content:center;gap:24px}
.arrow{position:absolute;top:80px;width:26px;height:26px;border-radius:50%;border:1px solid #bbb;display:flex;align-items:center;justify-content:center}
.arrow.prev{left:0}.arrow.next{right:0}
.card{width:226px;position:relative}
.card-photo{height:170px;border-radius:2px}
.card-label{position:absolute;right:0;bottom:-22px;width:150px;height:60px;background:var(--orange);color:var(--white);font-size:11px;font-weight:700;display:flex;align-items:center;justify-content:center;text-align:center;padding:0 12px 0 34px;line-height:1.3}
.card-icon{position:absolute;left:-20px;top:10px;width:40px;height:40px;border-radius:50%;background:var(--white);border:3px solid var(--orange);display:flex;align-items:center;justify-content:center}
.view-all{margin-top:60px}

.footer{position:absolute;left:0;top:920px;width:870px;height:252px;background:var(--forest);color:var(--white);display:flex;padding:28px 50px 0;gap:40px}
.footer h3{font-size:15px;font-weight:600;letter-spacing:.5px;margin-bottom:14px}
.col-contact{width:180px}
.col-news{width:170px}
.col-quote{width:200px}
.contact-row{display:flex;gap:8px;font-size:10px;line-height:1.5;margin-bottom:10px;color:#ddd}
.contact-row strong{color:var(--white)}
.news{list-style:none;font-size:10px;color:#ddd}
.news li{margin-bottom:12px;padding-left:12px;position:relative}
.news li::before{content:"";position:absolute;left:0;top:5px;width:4px;height:4px;background:var(--orange)}
.quote{font-size:10px;line-height:1.6;color:#ddd}
.quote-author{margin-top:10px;font-size:11px;color:var(--white)}
.footer-brand{flex:1;display:flex;flex-direction:column;align-items:center;padding-top:14px;gap:8px}
.footer-brand .brand-dot{width:50px;height:50px}
.footer-brand .brand-name{color:#a4d65e;font-size:14px}
.bottom-bar{position:absolute;left:0;top:1172px;width:870px;height:28px;background:var(--orange);color:var(--forest);font-size:10px;font-weight:600;display:flex;align-items:center;justify-content:center}
</style>
</head>
<body>
<div class="page">
  <header class="header">
    <div class="brand"><span class="brand-dot"></span><span class="brand-name">VELLORA</span></div>
    <div class="header-right">
      <div class="follow">FOLLOW US ON
        <span class="social"></span><span class="social"></span><span class="social"></span><span class="social"></span>
      </div>
      <div class="call">
        <svg width="22" height="22" viewBox="0 0 24 24"><path fill="#f39200" d="M6.6 10.8a15 15 0 0 0 6.6 6.6l2.2-2.2a1 1 0 0 1 1-.25 11.4 11.4 0 0 0 3.6.57 1 1 0 0 1 1 1V20a1 1 0 0 1-1 1A17 17 0 0 1 3 4a1 1 0 0 1 1-1h3.5a1 1 0 0 1 1 1c0 1.25.2 2.45.57 3.57a1 1 0 0 1-.25 1z"/></svg>
        <div class="call-label">Call Us Now<span class="call-number">(123) 456 7890</span></div>
      </div>
    </div>
  </header>

  <nav class="nav">
    <a>Assisted Living</a><a>Skilled Nursing</a><a>Independent Living</a><a>Home &amp; Community Based Living</a><a>Respite Care</a><a>Rehabilitation</a><a>SABD Learning</a>
  </nav>

  <section class="hero" role="img" aria-label="Smiling senior couple walking together in a sunny autumn park">
    <div class="hero-copy">
      <h1 class="hero-title">Live Independently in Your Communities</h1>
      <p class="hero-sub">Quality health care delivered at your door, in the comfort of your own home and community.</p>
      <div class="hero-actions"><span class="btn btn-dark">Learn More</span><span class="btn btn-orange">Join Now</span></div>
    </div>
  </section>

  <section class="services">
    <h2 class="section-title">STAY HOME</h2>
    <p class="section-text">Vellora offers Home and Community Based Services for adults who wish to continue to live independently in the comfort of their communities. We provide on site services and deliver high quality healthcare at your door. Our experienced physicians coordinate care with our certified nurse practitioners and provide chronic care management, physical therapy, rehabilitation and medications management.</p>
    <div class="cards">
      <span class="arrow prev"><svg width="10" height="10" viewBox="0 0 10 10"><path d="M7 1 3 5l4 4" stroke="#888" stroke-width="1.5" fill="none"/></svg></span>
      <div class="card">
        <div class="card-photo" role="img" aria-label="Nurse checking an elderly patient's blood pressure" style="background:linear-gradient(135deg,#dfe6ec,#b7c7d3)"></div>
        <div class="card-label"><span class="card-icon"><svg width="18" height="18" viewBox="0 0 20 20"><path d="M8 3h4v5h5v4h-5v5H8v-5H3V8h5z" fill="#f39200"/></svg></span>Comprehensive Primary Care Services</div>
      </div>
      <div class="card">
        <div class="card-photo" role="img" aria-label="Caregiver sitting with an elderly woman at home" style="background:linear-gradient(135deg,#e6e0d6,#c9bda9)"></div>
        <div class="card-label"><span class="card-icon"><svg width="18" height="18" viewBox="0 0 20 20"><path d="M4 10l4 4 8-8" stroke="#f39200" stroke-width="2.5" fill="none"/></svg></span>Coordination of specialty care</div>
      </div>
      <div class="card">
        <div class="card-photo" role="img" aria-label="Nurse assisting a senior patient in a care room" style="background:linear-gradient(135deg,#e9e4df,#cdbfb5)"></div>
        <div class="card-label"><span class="card-icon"><svg width="18" height="18" viewBox="0 0 20 20"><path d="M10 17s-7-4.5-7-9a4 4 0 0 1 7-2.5A4 4 0 0 1 17 8c0 4.5-7 9-7 9z" fill="#f39200"/></svg></span>Chronic Disease Management</div>
      </div>
      <span class="arrow next"><svg width="10" height="10" viewBox="0 0 10 10"><path d="M3 1l4 4-4 4" stroke="#888" stroke-width="1.5" fill="none"/></svg></span>
    </div>
    <div class="view-all"><span class="btn btn-dark">View All Services</span></div>
  </section>

  <footer class="footer">
    <div class="col-contact">
      <h3>CONTACT US</h3>
      <div class="contact-row"><svg width="12" height="14" viewBox="0 0 12 14"><path d="M6 0a5 5 0 0 1 5 5c0 4-5 9-5 9S1 9 1 5a5 5 0 0 1 5-5zm0 3a2 2 0 1 0 0 4 2 2 0 0 0 0-4z" fill="#fff"/></svg><span><strong>VELLORA</strong><br>123 Building name, Street Name,<br>City Country - Zipcode</span></div>
      <div class="contact-row"><svg width="12" height="12" viewBox="0 0 24 24"><path fill="#fff" d="M6.6 10.8a15 15 0 0 0 6.6 6.6l2.2-2.2a1 1 0 0 1 1-.25 11.4 11.4 0 0 0 3.6.57 1 1 0 0 1 1 1V20a1 1 0 0 1-1 1A17 17 0 0 1 3 4a1 1 0 0 1 1-1h3.5a1 1 0 0 1 1 1c0 1.25.2 2.45.57 3.57a1 1 0 0 1-.25 1z"/></svg><span>123-456-7890</span></div>
      <div class="contact-row"><svg width="12" height="10" viewBox="0 0 12 10"><rect x=".5" y=".5" width="11" height="9" fill="none" stroke="#fff"/><path d="M.5.5 6 5l5.5-4.5" fill="none" stroke="#fff"/></svg><span>info@vellora.com</span></div>
    </div>
    <div class="col-news">
      <h3>LATEST NEWS</h3>
      <ul class="news">
        <li>Lorem Ipsum is simply dummy</li>
        <li>Lorem Ipsum is simply dummy</li>
        <li>Lorem Ipsum is simply dummy</li>
        <li>Lorem Ipsum is simply dummy</li>
      </ul>
    </div>
    <div class="col-quote">
      <h3>TESTIMONIALS</h3>
      <p class="quote">"Lorem Ipsum is simply dummy text of the printing and typesetting industry. Lorem Ipsum has been the industry's standard"</p>
      <p class="quote-author">- Dana Morel</p>
    </div>
    <div class="footer-brand"><span class="brand-dot"></span><span class="brand-name">VELLORA</span></div>
  </footer>
  <div class="bottom-bar">© VELLORA 2017. All Rights Reserved.</div>
</div>
</body>
</html>
```